Drug Company Needs a Counter Display

********I am after a point of sale counter top display design. **********
^^^^^^^^^^^^^^^^^^^^^^^^^^^^^^^^^^^^^^^^^^^^^^^^^^

The design should somewhat match the current format of my products, be eye caching and modern. PLEASE REFERR TO THE ATTACHMENTS FOR INSPIRATION

What I had in mind for this project was;
If you can notice the counter display as shown in the picture with the products inside.
The bottom half of the product boxes have been cut off because of the front lip of the display, I was perhaps thinking that the display could have the bottom half of the box printed on it so it would give the illusion of a complete box.. This could be the same on the sides also, as it tapers up giving the illusion of a complete box.

I imagine possibly having the centre divider either black on the centre and then because the display is slightly larger than the boxes the "illusion" box on the left and right can be centered and then outlined with black lines.

The header board should have a clear catch phrase like "Drug Testing Kits"- easy to use -99% accuracy - fast results the text can be set on a contrasting background, solid colors are ok with gradients, swirls etc any graphic you think looks good.

Detection Times
*Depending on quantity
Ecstasy - 1 - 3 Days
Meth Amphetamine - 1 - 3 Days
Marijuana - 1 - 30 Days

This project is very open to creativity and designers can head in their own direction with this, I am not overly creative and my idea was only a suggestion.. I am keen to take on any eye catching yet professional design.

Thanks in advance.

Target Market(s)

Adults ages 18 - 45 in western speaking countries.

Industry/Entity Type

Drug

Requirements
Must have
• Easy to read text
Should not have
• cluttered text

```html
<!DOCTYPE html>
<html lang="en">
<head>
<meta charset="utf-8">
<title>Drug Testing Kit – Counter Header Board</title>
<link rel="stylesheet" href="https://fonts.googleapis.com/css2?family=Righteous&family=Arimo:wght@700&display=swap">
<style>
  :root {
    --page-bg: #ffffff;
    --board-deep: #020617;
    --board-navy: #0a1a4a;
    --board-mid: #13265e;
    --text-white: #ffffff;
    --accent-yellow: #e4ff2a;
    --divider-green: #5a7a3a;
    --shadow: rgba(0, 0, 0, 0.85);
  }
  * { margin: 0; padding: 0; box-sizing: border-box; }
  html, body {
    width: 1200px;
    height: 1000px;
    overflow: hidden;
    background: var(--page-bg);
  }
  .canvas {
    position: relative;
    width: 1200px;
    height: 1000px;
  }
  .header-board {
    position: absolute;
    left: 27px;
    top: 342px;
    width: 1144px;
    height: 315px;
    overflow: hidden;
    background: var(--board-navy);
    color: var(--text-white);
    text-align: center;
    font-family: "Arimo", Arial, sans-serif;
  }
  .swirl-backdrop {
    position: absolute;
    inset: 0;
    background:
      radial-gradient(ellipse 420px 150px at 50% 52%, var(--board-deep) 0%, rgba(6,14,40,0.9) 45%, rgba(19,38,94,0) 100%),
      radial-gradient(ellipse 700px 260px at 50% 50%, var(--board-mid) 0%, var(--board-navy) 70%, #0b1d55 100%);
  }
  .board-content { position: relative; }
  .headline {
    font-family: "Righteous", "Arial Black", sans-serif;
    font-size: 104px;
    line-height: 1;
    letter-spacing: 2px;
    padding-top: 10px;
    text-shadow: 4px 5px 6px var(--shadow);
  }
  .detection-label {
    display: inline-block;
    margin-top: 16px;
    padding: 2px 14px 4px;
    border: 2px solid var(--text-white);
    font-size: 31px;
    line-height: 1.2;
  }
  .detection-list {
    display: flex;
    justify-content: center;
    align-items: center;
    margin-top: 8px;
    font-size: 26px;
    line-height: 1.4;
  }
  .detection-item { padding: 0 12px; }
  .detection-divider {
    width: 4px;
    height: 44px;
    background: var(--divider-green);
  }
  .tagline {
    margin-top: 6px;
    font-size: 44px;
    line-height: 1.2;
    color: var(--accent-yellow);
    text-shadow: 2px 2px 3px var(--shadow);
  }
  .footnote {
    margin-top: 6px;
    font-size: 18px;
  }
</style>
</head>
<body>
  <main class="canvas">
    <section class="header-board">
      <div class="swirl-backdrop" role="img" aria-label="Dark navy background with a soft water-ripple swirl"></div>
      <div class="board-content">
        <h1 class="headline">Drug Testing Kit</h1>
        <div class="detection-label">Detection Times</div>
        <div class="detection-list">
          <span class="detection-item">Ecstasy - 1 - 3 Days</span>
          <span class="detection-divider"></span>
          <span class="detection-item">Meth Amphetamine - 1 - 3 Days</span>
          <span class="detection-divider"></span>
          <span class="detection-item">Marijuana - 1 - 30 Days</span>
        </div>
        <p class="tagline">easy to use -99% accuracy - fast results</p>
        <p class="footnote">*Depending on quantity</p>
      </div>
    </section>
  </main>
</body>
</html>
```